Dorsey K. Whitfield Business Card

We need a business card for our company Dorsey K. Whitfield Heating & Plumbing to be distributed to potential customers. It should follow the color scheme of our logo and have a modern upscale and masculine look.

The logo is attached and the info below should also be included:

5187 W. Quarry Bend Rd.
Manheim, PA 17545

Tobias R. Whitfield
(717) 593-8126
tobiasreedwhitfield@mailvane.com
dorseykwhitfield.com
PA #038419

Industry/Entity Type

Business

Contact Information for Business Card

5187 W. Quarry Bend Rd.
Manheim, PA 17545

Tobias R. Whitfield
(717) 593-8126
tobiasreedwhitfield@mailvane.com
dorseykwhitfield.com
PA #038419

Colors

Designer to choose colors to be used in the design.

Requirements
Must have
• Information above included

```html
<!DOCTYPE html>
<html lang="en">
<head>
<meta charset="utf-8">
<title>Dorsey K. Whitfield Heating &amp; Plumbing — Business Card</title>
<link rel="stylesheet" href="https://fonts.googleapis.com/css2?family=Open+Sans:wght@400;700&display=swap">
<style>
  :root {
    --brand-blue: #0d5aa7;
    --brand-blue-dark: #0a4a8c;
    --brand-green: #8dc63f;
    --ink: #4a4a4a;
    --paper: #ffffff;
    --backdrop: #e4e6e9;
    --divider: #c9cccf;
  }
  * { margin: 0; padding: 0; box-sizing: border-box; }
  html, body {
    width: 1200px; height: 960px; overflow: hidden;
    background: var(--backdrop);
    font-family: "Open Sans", Arial, sans-serif;
  }
  .card {
    position: absolute;
    width: 700px; height: 400px;
    left: 250px;
    box-shadow: 0 6px 24px rgba(0,0,0,.18);
    overflow: hidden;
  }

  /* Back side */
  .card-back {
    top: 60px;
    background: linear-gradient(135deg, #1466bb 0%, var(--brand-blue) 55%, var(--brand-blue-dark) 100%);
    display: flex; align-items: center; justify-content: center;
  }
  .wordmark {
    display: flex; align-items: center; gap: 16px;
    font-weight: 700; line-height: 1.1;
  }
  .wordmark-square { width: 52px; height: 52px; flex: none; }
  .card-back .wordmark { color: var(--paper); font-size: 30px; }
  .card-back .wordmark-square { background: var(--paper); }

  /* Front side */
  .card-front { top: 500px; background: var(--paper); }
  .card-front .wordmark {
    position: absolute; left: 40px; top: 112px; width: 280px;
    color: var(--brand-blue); font-size: 24px;
  }
  .card-front .wordmark-square { background: var(--brand-blue); width: 44px; height: 44px; }

  .divider {
    position: absolute; left: 345px; top: 96px;
    width: 1px; height: 190px;
    background: linear-gradient(to bottom, transparent, var(--divider) 20%, var(--divider) 80%, transparent);
  }

  .contact { position: absolute; left: 372px; top: 100px; color: var(--ink); }
  .contact-name {
    color: var(--brand-blue); font-weight: 700; font-size: 24px;
    text-transform: uppercase; margin-bottom: 10px;
  }
  .contact-address { font-size: 17px; line-height: 1.3; margin-bottom: 8px; }
  .contact-line { display: flex; align-items: center; gap: 8px; font-size: 16px; line-height: 1.45; }
  .contact-line svg { width: 16px; height: 16px; flex: none; fill: var(--brand-blue); }

  .web-band {
    position: absolute; left: 0; top: 290px; width: 470px; height: 40px;
    background: var(--brand-blue);
    color: var(--paper); font-size: 17px; letter-spacing: 5px;
    display: flex; align-items: center; padding-left: 50px;
  }
  .accent-square {
    position: absolute; left: 476px; top: 330px; width: 40px; height: 40px;
    background: var(--brand-blue);
  }
  .accent-bar {
    position: absolute; left: 522px; top: 330px; right: 0; height: 40px;
    background: var(--brand-green);
  }
</style>
</head>
<body>

<section class="card card-back" aria-label="Business card, back">
  <div class="wordmark">
    <span class="wordmark-square"></span>
    <span class="wordmark-name">Dorsey K. Whitfield<br>Heating &amp; Plumbing</span>
  </div>
</section>

<section class="card card-front" aria-label="Business card, front">
  <div class="wordmark">
    <span class="wordmark-square"></span>
    <span class="wordmark-name">Dorsey K. Whitfield<br>Heating &amp; Plumbing</span>
  </div>

  <div class="divider"></div>

  <div class="contact">
    <p class="contact-name">Tobias R. Whitfield</p>
    <p class="contact-address">5187 W. Quarry Bend Rd.<br>Manheim, PA 17545<br>PA #038419</p>
    <p class="contact-line">
      <svg viewBox="0 0 16 16" aria-hidden="true"><path d="M3 5c0-2 2-3 5-3s5 1 5 3v1h-3V5H6v1H3zM4 7h8l2 7H2z M8 9a2 2 0 1 0 .01 0z"/></svg>
      (717) 593-8126
    </p>
    <p class="contact-line">
      <svg viewBox="0 0 16 16" aria-hidden="true"><path d="M1 3h14v10H1zM2 4l6 5 6-5z" fill-rule="evenodd"/></svg>
      tobiasreedwhitfield@mailvane.com
    </p>
  </div>

  <div class="web-band">www.dorseykwhitfield.com</div>
  <div class="accent-square"></div>
  <div class="accent-bar"></div>
</section>

</body>
</html>
```